UI Kit for Contractor Websites

I created a wireframe in Webflow and want to create a number of templates around that. There are existing templates, but I a few built around my content structure.

The types of clients are home remodeling services (homebuilders, plumbers, painters, electricians, handymen, etc.)

https://site-draft-7bc41d90e28-f5a2b9c03d71e.pagebuild.example/

*Use the website copy content from here but you do NOT need to follow the wireframe so plug it in however you feel best. Eventually, we'll have multiple types of heroes, services, etc.

I'd like to start with the first homepage template. The homepage templates will all have the same fonts, color scheme, and content. Once we finish about 5 of those, we'd move onto the next stage.

https://www.clipnest.example/share/9f4e1b7a2c6d48e0b3a5f71c2d8e6b04

Other clean, modern, UI kits (templates) or websites I like:
https://www.brivola.example/
https://harbor-template.pagebuild.example/
https://quillet.example/
https://fern-template.pagebuild.example/
https://www.pagewell.example/tidemark-website-templates
https://vantage-template.pagebuild.example/
https://tiles-template.pagebuild.example/

*We'd likely have a lot of images, not illustrations since the client type we're building is pretty visual. Can use dummy photos.

Home

Navbar

Hero Section
Preheader (H1)
Hero Header (H2)
Hero CTA
Hero Secondary CTA

Hero Testimonial Short Quote
Hero Testimonial Name

Social Proof (CMS, can be multiple or one)
Testimonial Quote
Testimonial Name
Testimonial Image

CTA
CTA Headline
CTA Subheadline
CTA Button

Features/Value Stack
Value Stack H2
Value 1 Headline (H3)
Value 1 Description
Value 2 Headline (H3)
Value 2 Description
Value 3 Headline (H3)
Value 3 Description

Services (CMS, can be multiple)
Service Name
Service Short Description
CTA: Get Quote
Main Image

Homepage How It Works
Homepage How It Works Headline
How it Works Subheadline
Step 1 Name
Step 1 Description
Step 2 Name
Step 2 Description
Step 3 Name
Step 3 Description

About/Founder’s Note/Team
Homepage Founder Note Headline
Founder Note or About Info
Owner Signature
CTA to About Page

CTA
CTA Headline
CTA Subheadline
CTA Button

Footer

```html
<!DOCTYPE html>
<html lang="en">
<head>
<meta charset="utf-8">
<title>Hearthwell — Home Remodeling Services</title>
<link href="https://fonts.googleapis.com/css2?family=Rubik:wght@400;500;600&family=Arimo:wght@400;700&family=Nothing+You+Could+Do&display=swap" rel="stylesheet">
<style>
:root{
  --yellow:#f8b617;
  --yellow-soft:#fdf0c8;
  --black:#0c0c0c;
  --ink:#1a1a1a;
  --grey:#6f6f6f;
  --white:#ffffff;
}
*{margin:0;padding:0;box-sizing:border-box}
html,body{width:1200px;height:4644px;overflow:hidden}
body{position:relative;font-family:"Arimo",Arial,sans-serif;color:var(--ink);background:var(--white)}
.abs{position:absolute}
h1,h2,h3{font-family:"Rubik",Arial,sans-serif;font-weight:500}
.accent{color:var(--yellow)}
.btn{position:absolute;display:flex;align-items:center;justify-content:center;font-family:"Rubik",sans-serif;font-weight:600;font-size:13px;text-transform:uppercase;color:var(--ink);background:var(--yellow)}
.photo{position:absolute}

/* header + hero */
.hero{position:absolute;left:0;top:0;width:1200px;height:636px;background:var(--yellow)}
.logo{position:absolute;font-family:"Rubik",sans-serif;font-weight:500;font-size:29px;letter-spacing:-.5px}
.nav{position:absolute;left:576px;top:28px;height:20px;border-left:1px solid rgba(255,255,255,.8);display:flex;gap:22px;padding-left:14px;font-size:12px;color:var(--white)}
.call{position:absolute;left:998px;top:22px;display:flex;gap:10px;align-items:center}
.call small{display:block;font-size:10px;color:var(--white)}
.call b{font-size:15px;color:var(--ink)}
.hero .pre{left:61px;top:180px;font-size:12px;color:var(--white)}
.hero h1{position:absolute;left:59px;top:200px;font-size:40px;line-height:47px;color:var(--ink)}
.hero h1 .lead{color:var(--white)}
.hero .intro{left:61px;top:306px;width:360px;font-size:11.5px;line-height:19px;color:var(--ink)}
.hero .quote-btn{left:60px;top:360px;width:136px;height:41px;background:transparent;border:1.5px solid var(--ink)}
.hero .avatar{left:60px;top:463px;width:62px;height:62px;border-radius:50%;background:linear-gradient(135deg,#b27b55,#5a3a28)}
.hero .mini-quote{left:137px;top:468px;width:300px;font-size:11px;line-height:19px;color:var(--white)}
.hero .mini-quote b{color:var(--ink);margin-left:4px}
.hero-photo{left:518px;top:128px;width:622px;height:582px;background:linear-gradient(160deg,#d7c9b2,#8e7a62 60%,#4a4038)}
.scroll{left:1160px;top:400px;transform:rotate(-90deg);transform-origin:left top;font-size:10px;color:var(--white);white-space:nowrap}

/* testimonials */
.section-title{position:absolute;left:0;width:1200px;text-align:center;font-family:"Rubik",sans-serif;font-weight:500;font-size:31px;line-height:42px}
.card{position:absolute;top:899px;width:300px;height:209px;border:1.5px solid var(--yellow);border-radius:10px;background:var(--white)}
.card .badge{position:absolute;left:-1px;top:-1px;width:42px;height:42px;background:var(--yellow);border-radius:10px 0 20px 0;display:flex;align-items:center;justify-content:center}
.card p{position:absolute;left:30px;top:36px;width:250px;font-size:11px;line-height:20px;color:var(--grey)}
.card .face{position:absolute;left:32px;top:131px;width:52px;height:52px;border-radius:50%;background:linear-gradient(135deg,#caa58a,#6b4b38)}
.card .who{position:absolute;left:98px;top:143px;font-size:11px;color:var(--yellow)}
.card .site{position:absolute;left:122px;top:163px;font-size:11px;color:var(--grey)}

/* struggle */
.struggle h2{position:absolute;left:654px;top:1203px;font-size:32px;line-height:38px}
.struggle .lead{left:655px;top:1286px;width:390px;font-size:11.5px;line-height:20px;color:var(--grey)}
.struggle ul{position:absolute;left:658px;top:1347px;list-style:none;font-size:11.5px;color:var(--grey)}
.struggle li{height:29px;display:flex;align-items:flex-start;gap:14px}
.struggle li::before{content:"";width:8px;height:8px;margin-top:3px;border:2px solid var(--yellow);border-radius:50%}
.struggle .better{left:651px;top:1503px;font-size:13px;color:var(--yellow)}

/* services */
.svc{position:absolute;width:435px;height:293px;overflow:hidden;background:var(--yellow-soft)}
.svc.dark{background:var(--black)}
.svc h3{position:absolute;left:0;width:100%;top:50px;text-align:center;font-size:19px;color:var(--ink)}
.svc.dark h3{color:var(--yellow)}
.svc p{position:absolute;left:55px;width:325px;top:84px;text-align:center;font-size:11px;line-height:20px;color:var(--grey)}
.svc.dark p{color:var(--white)}
.svc .service-image{position:absolute;left:77px;top:150px;width:280px;height:143px}

/* features */
.features{position:absolute;left:0;top:2563px;width:1200px;height:405px;background:var(--black)}
.feat-photo{left:90px;top:2496px;width:382px;height:394px;background:linear-gradient(150deg,#b9a38a,#6e5a48 55%,#3a3029);border-left:3px solid var(--yellow)}
.features h2{position:absolute;left:528px;top:55px;font-size:30px;color:var(--white)}
.features .lead{left:531px;top:106px;font-size:11.5px;color:var(--white)}
.value{position:absolute;top:158px;width:180px;color:var(--white)}
.value h3{margin-top:20px;font-family:"Arimo",sans-serif;font-weight:700;font-size:14px}
.value p{margin-top:16px;font-size:10.5px;line-height:19px;color:#cfcfcf}

/* how it works */
.how{position:absolute;left:0;top:2968px;width:1200px;height:487px;background:var(--yellow)}
.how h2{position:absolute;left:0;width:1200px;top:82px;text-align:center;font-size:30px;color:var(--white)}
.how h2 span{color:var(--ink)}
.how .lead{left:0;width:1200px;top:128px;text-align:center;font-size:11.5px;color:var(--ink)}
.step{position:absolute;top:180px;width:240px;text-align:center}
.step .num{position:absolute;left:32px;top:0;font-family:"Rubik",sans-serif;font-size:120px;line-height:120px;color:transparent;-webkit-text-stroke:1.5px rgba(255,255,255,.55)}
.step .dot{position:absolute;left:96px;top:14px;width:84px;height:84px;border-radius:50%;background:rgba(255,255,255,.35);display:flex;align-items:center;justify-content:center}
.step .dot span{width:62px;height:62px;border-radius:50%;background:var(--black);display:flex;align-items:center;justify-content:center}
.step h3{position:absolute;left:0;width:100%;top:140px;font-family:"Arimo",sans-serif;font-weight:700;font-size:14.5px;color:var(--ink)}
.step p{position:absolute;left:10px;width:220px;top:168px;font-size:11px;line-height:20px;color:var(--white)}

/* mission */
.mission h2{position:absolute;left:144px;top:3528px;font-size:32px}
.mission .lead{left:144px;top:3584px;width:380px;font-size:12.5px;line-height:20px;color:var(--ink)}
.mission .body{left:144px;width:380px;font-size:11px;line-height:20px;color:var(--grey)}
.mission .sign{left:144px;top:3825px;font-family:"Nothing You Could Do",cursive;font-size:19px;color:var(--ink)}
.mission-photo{left:668px;top:3455px;width:412px;height:540px;background:linear-gradient(160deg,#e6e2da,#b8a48a 55%,#5e4c3a)}

/* ready */
.ready .sub{left:0;width:1200px;top:4104px;text-align:center;font-size:13px}
.ready .body{left:310px;width:580px;top:4148px;text-align:center;font-size:11.5px;line-height:20px;color:var(--grey)}

/* footer */
.footer{position:absolute;left:0;top:4340px;width:1200px;height:304px;background:var(--black);color:var(--white)}
.footer .ask{left:0;width:1200px;top:48px;text-align:center;font-family:"Rubik",sans-serif;font-weight:500;font-size:21px;color:var(--yellow)}
.footer .phone{left:0;width:1200px;top:91px;text-align:center;font-size:22px}
.footer .mail{left:0;width:1200px;top:132px;text-align:center;font-size:11.5px}
.social{position:absolute;top:78px;width:36px;height:36px;border-radius:50%;background:var(--yellow)}
.footer .rule{left:62px;top:204px;width:1076px;height:1px;background:#2c2c2c}
.footer .links{left:0;width:1200px;top:228px;text-align:center;font-size:11px}
.footer .copy{left:0;width:1200px;top:257px;text-align:center;font-size:11px}
</style>
</head>
<body>

<header class="hero">
  <div class="logo" style="left:60px;top:22px"><span style="color:var(--white)">HEARTHWELL</span></div>
  <nav class="nav"><span>Home</span><span>Features</span><span>How It Works</span><span>About Us</span><span>Contact Us</span></nav>
  <div class="call">
    <svg width="28" height="28" viewBox="0 0 24 24"><path d="M6.6 10.8a15 15 0 0 0 6.6 6.6l2.2-2.2a1 1 0 0 1 1-.25 11 11 0 0 0 3.6.6 1 1 0 0 1 1 1V20a1 1 0 0 1-1 1A17 17 0 0 1 3 4a1 1 0 0 1 1-1h3.5a1 1 0 0 1 1 1 11 11 0 0 0 .6 3.6 1 1 0 0 1-.25 1z" fill="var(--ink)"/></svg>
    <div><small>Call Us</small><b>555 014 2760</b></div>
  </div>
  <div class="abs pre">YOUR HOME AS YOU WANT</div>
  <h1><span class="lead">Expert</span> In Home<br>Remodeling Services</h1>
  <p class="abs intro">Lorem Ipsum has been the industry's standard dummy text ever since the when an unknown printer took</p>
  <div class="btn quote-btn">Get A Quote</div>
  <div class="abs avatar" role="img" aria-label="Portrait of a smiling client"></div>
  <p class="abs mini-quote">Lorem ipsum has been the industry's standard dummy text ever since the when an unknown printer -<b>Client Name</b></p>
  <div class="abs scroll">Scroll Down</div>
</header>
<div class="photo hero-photo" role="img" aria-label="Three smiling contractors in hard hats and work overalls giving thumbs up"></div>

<section class="testimonials">
  <h2 class="section-title" style="top:780px">What Our Happy Client Say About<br><span class="accent">Hearthwell</span></h2>
  <div class="card" style="left:127px">
    <div class="badge"><svg width="20" height="14" viewBox="0 0 20 14"><path d="M0 14V7Q0 1 6 0v3Q3 4 3 7h4v7zM11 14V7q0-6 6-7v3q-3 1-3 4h4v7z" fill="#fff"/></svg></div>
    <p>" Lorem Ipsum has been the industry's stand dummy text ever since thes, when unknown printer took a galley of type and scrambled it to make a type specimen book."</p>
    <div class="face" role="img" aria-label="Client portrait"></div>
    <div class="who">—&nbsp;&nbsp;CLIENT NAME</div><div class="site">hearthwell.example</div>
  </div>
  <div class="card" style="left:449px">
    <div class="badge"><svg width="20" height="14" viewBox="0 0 20 14"><path d="M0 14V7Q0 1 6 0v3Q3 4 3 7h4v7zM11 14V7q0-6 6-7v3q-3 1-3 4h4v7z" fill="#fff"/></svg></div>
    <p>" Lorem Ipsum has been the industry's stand dummy text ever since thes, when unknown printer took a galley of type and scrambled it to make a type specimen book."</p>
    <div class="face" role="img" aria-label="Client portrait"></div>
    <div class="who">—&nbsp;&nbsp;CLIENT NAME</div><div class="site">hearthwell.example</div>
  </div>
  <div class="card" style="left:771px">
    <div class="badge"><svg width="20" height="14" viewBox="0 0 20 14"><path d="M0 14V7Q0 1 6 0v3Q3 4 3 7h4v7zM11 14V7q0-6 6-7v3q-3 1-3 4h4v7z" fill="#fff"/></svg></div>
    <p>" Lorem Ipsum has been the industry's stand dummy text ever since thes, when unknown printer took a galley of type and scrambled it to make a type specimen book."</p>
    <div class="face" role="img" aria-label="Client portrait"></div>
    <div class="who">—&nbsp;&nbsp;CLIENT NAME</div><div class="site">hearthwell.example</div>
  </div>
</section>

<section class="struggle">
  <div class="photo" style="left:157px;top:1210px;width:150px;height:281px;background:linear-gradient(160deg,#f3d36b,#c99a3a)" role="img" aria-label="Worker installing a ceiling light"></div>
  <div class="photo" style="left:316px;top:1210px;width:267px;height:281px;background:linear-gradient(160deg,#efe9e1,#b59c82 60%,#6c5a4a)" role="img" aria-label="Remodeled living room with built-in shelving"></div>
  <h2>Do You<br><span class="accent">Struggle With</span></h2>
  <p class="abs lead">Lorem Ipsum has been the industry's standard dummy text ever since the when an unknown printer took.</p>
  <ul>
    <li>Lorem Ipsum has been the industry standard</li>
    <li>It has survived not only five centuries.</li>
    <li>Lorem Ipsum has been the industry standard</li>
    <li>It has survived not only five centuries.</li>
    <li>Lorem Ipsum has been the industry standard</li>
  </ul>
  <div class="abs better">...well we've found a better way.</div>
  <div class="btn" style="left:654px;top:1533px;width:135px;height:40px">Learn More</div>
</section>

<section class="services">
  <h2 class="section-title" style="top:1643px">Our <span class="accent">Services</span></h2>
  <div class="abs" style="left:0;width:1200px;top:1689px;text-align:center;font-size:11.5px">What We Offer</div>

  <div class="svc dark" style="left:141px;top:1742px">
    <h3>Plumbers</h3><p>Lorem Ipsum has been the industry's standard dummy text ever since the when an printer</p>
    <div class="service-image" role="img" aria-label="Plumber holding a wrench" style="background:linear-gradient(180deg,#3a3a3a,#1f2a3c)"></div>
  </div>
  <div class="svc" style="left:598px;top:1742px">
    <h3>Painters</h3><p>Lorem Ipsum has been the industry's standard dummy text ever since the when an printer</p>
    <div class="service-image" role="img" aria-label="Painter in overalls holding a paint roller" style="background:linear-gradient(180deg,#f4d88a,#c9a04a)"></div>
  </div>
  <div class="svc" style="left:141px;top:2058px">
    <h3>Electricians</h3><p>Lorem Ipsum has been the industry's standard dummy text ever since the when an printer</p>
    <div class="service-image" role="img" aria-label="Electrician in a white hard hat working on a panel" style="background:linear-gradient(180deg,#f4d88a,#c9a04a)"></div>
  </div>
  <div class="svc" style="left:598px;top:2058px">
    <h3>Handymen</h3><p>Lorem Ipsum has been the industry's standard dummy text ever since the when an printer</p>
    <div class="service-image" role="img" aria-label="Handyman holding several tools" style="background:linear-gradient(180deg,#f4d88a,#c9a04a)"></div>
  </div>
  <div class="btn" style="left:498px;top:2380px;width:203px;height:40px">Explore All Services</div>
</section>

<section class="features">
  <h2>Our <span class="accent">Features</span></h2>
  <p class="abs lead">Lorem Ipsum has been the industry's standard dummy text ever since the text.</p>
  <div class="value" style="left:531px">
    <svg width="46" height="46" viewBox="0 0 46 46" fill="none" stroke="var(--yellow)" stroke-width="2"><path d="M6 28a17 17 0 0 1 34 0M4 28h38v5H4zM23 11v17M15 14l3 14M31 14l-3 14M10 36q13 8 26 0"/></svg>
    <h3>Value 1</h3><p>Lorem Ipsum has been the industry's standard dummy text ever since the..</p>
  </div>
  <div class="value" style="left:731px">
    <svg width="46" height="46" viewBox="0 0 46 46" fill="none" stroke="var(--yellow)" stroke-width="2"><rect x="6" y="4" width="22" height="36" rx="2"/><rect x="10" y="9" width="14" height="9"/><path d="M12 24h3M19 24h3M12 30h3M19 30h3M34 8v30M30 14h8v24h-8z"/></svg>
    <h3>Value 1</h3><p>Lorem Ipsum has been the industry's standard dummy text ever since the..</p>
  </div>
  <div class="value" style="left:931px">
    <svg width="46" height="46" viewBox="0 0 46 46" fill="none" stroke="var(--yellow)" stroke-width="2"><path d="M4 22 23 6l19 16M9 18v22h28V18M17 40V28h12v12M28 8l8-4 4 8"/></svg>
    <h3>Value 1</h3><p>Lorem Ipsum has been the industry's standard dummy text ever since the..</p>
  </div>
</section>
<div class="photo feat-photo" role="img" aria-label="Contractor studying plans at a workbench with a colleague on a ladder behind"></div>

<section class="how">
  <h2>How It <span>Works</span></h2>
  <p class="abs lead">Lorem Ipsum has been the industry's standard dummy text ever since the text.</p>
  <div class="step" style="left:190px">
    <div class="num">1</div>
    <div class="dot"><span><svg width="22" height="26" viewBox="0 0 22 26" fill="none" stroke="var(--yellow)" stroke-width="2"><rect x="2" y="2" width="18" height="22" rx="2"/><path d="M6 6h10v5H6zM6 15h2M10 15h2M14 15h2M6 19h2M10 19h2M14 19h2"/></svg></span></div>
    <h3>Get A Quote</h3><p>Lorem ipsum dolor sit amet, consectetur adip the iscing elit, sed do eiusmod the tempor incidi.</p>
  </div>
  <div class="step" style="left:481px">
    <div class="num">2</div>
    <div class="dot"><span><svg width="22" height="26" viewBox="0 0 22 26" fill="none" stroke="var(--yellow)" stroke-width="2"><rect x="2" y="4" width="18" height="20" rx="2"/><path d="M7 2h8v4H7zM6 12h10M6 16h10M6 20h6"/></svg></span></div>
    <h3>We Do The Job</h3><p>Lorem ipsum dolor sit amet, consectetur adip the iscing elit, sed do eiusmod the tempor incidi.</p>
  </div>
  <div class="step" style="left:771px">
    <div class="num">3</div>
    <div class="dot"><span><svg width="26" height="24" viewBox="0 0 26 24" fill="var(--yellow)"><path d="M13 2 1 12h3v10h18V12h3zM10 22v-6h6v6z"/></svg></span></div>
    <h3 style="top:136px">Show Off Your House</h3><p style="top:164px">Lorem ipsum dolor sit amet, consectetur adip the iscing elit, sed do eiusmod the tempor incidi.</p>
  </div>
</section>

<section class="mission">
  <h2>Our <span class="accent">Mission</span></h2>
  <p class="abs lead">Lorem ipsum dolor sit amet, consectetur adipiscing elit, sed do eiusmod tempor incididunt ut labore.</p>
  <p class="abs body" style="top:3640px">Lorem ipsum dolor sit amet, consectetur adipiscing elit, sed do eiusmod tempor incididunt ut labore et dolore magna aliqua in Lorem ipsum dolor sit amet.</p>
  <p class="abs body" style="top:3712px">Lorem ipsum dolor sit amet, consectetur adipiscing elit, sed do eiusmod tempor incididunt ut labore et dolore magna th aliqua in. Lorem ipsum dolor sit amet, consectetur adipi is scing elit, sed do eiusmod tempor incididunt ut labore magn aliqua Lorem ipsum dolor sit amet, consectetur.</p>
  <div class="abs sign">Mara L. Owner</div>
  <div class="btn" style="left:144px;top:3872px;width:158px;height:39px">Meet Our Team</div>
</section>
<div class="photo mission-photo" role="img" aria-label="Smiling craftsman in a plaid shirt and apron holding a clipboard"></div>

<section class="ready">
  <h2 class="section-title" style="top:4052px">Ready <span class="accent">To Start?</span></h2>
  <div class="abs sub">So Are We. Let's go.</div>
  <p class="abs body">Lorem ipsum dolor sit amet, consectetur adipiscing elit, sed do eiusmod tempor incididunt ut labore et dolore the magna th aliqua Lorem ipsum dolor sit amet, consec this tetur adipi is scing elit, sed do eiusmod.</p>
  <div class="btn" style="left:533px;top:4222px;width:135px;height:40px">Get Started</div>
</section>

<footer class="footer">
  <div class="logo" style="left:62px;top:80px;color:var(--yellow)">HEARTHWELL</div>
  <div class="abs ask">Have An Question?</div>
  <div class="abs phone">555 014 2760</div>
  <div class="abs mail">info@hearthwell.example</div>
  <div class="social" style="left:1015px" role="img" aria-label="Social profile link"></div>
  <div class="social" style="left:1058px" role="img" aria-label="Social profile link"></div>
  <div class="social" style="left:1102px" role="img" aria-label="Social profile link"></div>
  <div class="abs rule"></div>
  <div class="abs links">Home&nbsp; | &nbsp;Features&nbsp; | &nbsp;How It Works&nbsp; | &nbsp;About Us&nbsp; | &nbsp;Contact Us</div>
  <div class="abs copy"><span class="accent">©HEARTHWELL</span> -2021 All rights reserved.</div>
</footer>

</body>
</html>
```